Marks of Dunmore business card design

I need a clean, professional looking design using the attached logo with a bright green/ gray/dark gray/black colors. Maybe even an orange accent if it looks good. I am open to slight changes in the logo if needed. Details below on the info on what should be on the cards. We are a sign company in Ft. Lauderdale FL that specializes in yacht lettering on multi million dollar yachts.

Target Market(s)

marine industry, yachts

Industry/Entity Type

Business

Colors
9bcb3c
000000
606060
f37122

Requirements
Must have
• address: 2847 W. Harlow Rd.
• Pompano Beach, FL 33417
• Phone: 954-518-3046
• email/website: marksofdunmore@mailvista.net MarksofDunmore.net
Nice to have
• I would like it very clean and simple but professional looking. Nice layout and would prefer a darker background. Orange highlight only if it works.
Should not have
• Nothing fancy.

```html
<!DOCTYPE html>
<html lang="en">
<head>
<meta charset="utf-8">
<title>Marks of Dunmore — Business Card</title>
<link href="https://fonts.googleapis.com/css2?family=Open+Sans:wght@400;600;800&display=swap" rel="stylesheet">
<style>
  :root {
    --backdrop: #1c1c1c;
    --lime: #9bcb3c;
    --brand-green: #0f9a3e;
    --paper: #ffffff;
    --ink: #606060;
    --rule: #9a9a9a;
  }
  * { margin: 0; padding: 0; box-sizing: border-box; }
  html, body {
    width: 1200px; height: 1200px; overflow: hidden;
    background: var(--backdrop);
    font-family: "Open Sans", sans-serif;
  }
  .canvas { position: relative; width: 1200px; height: 1200px; }
  .card {
    position: absolute; left: 250px; width: 700px; height: 400px;
    box-shadow: 0 14px 40px rgba(0,0,0,.55);
  }
  .card--front { top: 140px; background: var(--lime); display: flex; align-items: center; justify-content: center; }
  .card--back { top: 660px; background: var(--paper); }

  .wordmark { font-weight: 800; letter-spacing: .5px; white-space: nowrap; line-height: 1.1; }
  .card--front .wordmark { color: var(--paper); font-size: 52px; }
  .card--back .wordmark {
    position: absolute; left: 62px; top: 92px;
    color: var(--brand-green); font-size: 34px;
  }

  .identity { position: absolute; right: 62px; top: 66px; text-align: right; }
  .identity__name { color: var(--brand-green); font-weight: 600; font-size: 24px; letter-spacing: .3px; line-height: 1.3; }
  .identity__title { color: var(--ink); font-size: 15px; line-height: 1.3; }
  .identity-rule {
    position: absolute; left: 62px; right: 62px; top: 152px;
    height: 1px; background: var(--rule);
  }
  .address {
    position: absolute; right: 62px; top: 166px; text-align: right;
    color: var(--ink); font-size: 16px; line-height: 1.45;
  }

  .contact {
    position: absolute; left: 62px; bottom: 48px;
    border-top: 1px solid var(--rule); padding-top: 10px; width: 310px;
  }
  .contact__item {
    display: flex; align-items: center; gap: 10px;
    color: var(--ink); font-size: 17px; line-height: 1.5;
  }
  .contact__icon { width: 15px; height: 15px; flex: none; fill: var(--brand-green); }
</style>
</head>
<body>
<main class="canvas">
  <section class="card card--front" aria-label="Card front">
    <span class="wordmark">Marks of Dunmore</span>
  </section>

  <section class="card card--back" aria-label="Card back">
    <span class="wordmark">Marks of Dunmore</span>

    <div class="identity">
      <div class="identity__name">DANIEL MOREAU</div>
      <div class="identity__title">General Manager</div>
    </div>
    <div class="identity-rule"></div>
    <div class="address">2847 W. Harlow Rd.<br>Pompano Beach, FL 33417</div>

    <div class="contact">
      <div class="contact__item">
        <svg class="contact__icon" viewBox="0 0 16 16" aria-hidden="true"><path d="M3.6 1.2l2.2 2.6-1.3 1.6c.9 2 2.3 3.4 4.2 4.3l1.6-1.3 2.6 2.2-1.1 2.2c-5.6-.4-9.6-4.4-10-10z"/></svg>
        <span>954-518-3046</span>
      </div>
      <div class="contact__item">
        <svg class="contact__icon" viewBox="0 0 16 16" aria-hidden="true"><path d="M1 3h14v10H1z M2.2 4.2L8 8.8l5.8-4.6z" fill-rule="evenodd"/></svg>
        <span>marksofdunmore@mailvista.net</span>
      </div>
      <div class="contact__item">
        <svg class="contact__icon" viewBox="0 0 16 16" aria-hidden="true"><circle cx="8" cy="8" r="6.5" fill="none" stroke="#0f9a3e" stroke-width="1.4"/><path d="M1.5 8h13M8 1.5v13" stroke="#0f9a3e" stroke-width="1.1"/><ellipse cx="8" cy="8" rx="3" ry="6.5" fill="none" stroke="#0f9a3e" stroke-width="1.1"/></svg>
        <span>www.MarksofDunmore.net</span>
      </div>
    </div>
  </section>
</main>
</body>
</html>
```